A4 Tri-fold Brochure for Sedation Dentist Specialist Dr. Marlon and Sedation Dentistry.

I would like to create an A4 tri-fold brochure for our Dental Sedation Specialist Dr. Marlon Vesk. Please carefully select the most suitable highlights from his bio below.

This brochure has two parts. Highlighting what makes Dr. Marlon Vesk unique and trustworthy. Include a picture of him (attached). The second part is about sedation dentistry. All you need to know here: http://www.calmchairplex.com/how-does-sedation-dentistry-work

Avoid making it too wordy.

Meet Dr. Roh Dak Marlon Vesk, DDS

Inspired to Become a Dentist:
As a child, Dr. Marlon Vesk always felt stressed whenever he had to see a dentist. He knew that he wanted to become a dentist to help put patients completely at ease while they experienced quality dental care.

He is passionate about giving patients the healthy, beautiful smiles they deserve. “I find it fulfilling when I can see my patients’ beautiful smiles and how they can finally appreciate the joy of eating with a healthy set of teeth. However, what I love most about my job is the ability to provide a stress-free and comfortable experience at the dentist’s office, particularly for children, through sedation and general anesthesia.”

Educational Achievements:
Before becoming a dentist, Dr. Marlon Vesk earned his undergraduate degree at the Pellridge University of Northern Basin where he received a Bachelor of Medical Science Honor Specialization degree with distinction in biochemistry. He then completed his Doctor of Dental Surgery degree with honors at the Harwick Crest University. While there, he received the Elmer Drayce Medal in his class for outstanding achievement in anesthesia. He then pursued his three-year residency as well as a master’s degree in dental anesthesia at the Harwick Crest University.

So he can provide his patients with the latest in dentistry, Dr. Marlon Vesk enjoys pursuing additional knowledge, particularly in the areas of dental anesthesia as well as advanced technologies in dentistry. He is currently part of the Molar Horizon Circle study club and has enrolled in the Core Rootwork Mini- Residency Program. He also serves as a clinical instructor at the Plenvo Center at the Harwick Crest University.

Association Memberships:
In addition to his academic credentials, Dr. Marlon Vesk is a member of several associations:
The Vantley Board of Dental Surgeons of Quarrow (VBDSQ)
Dental Norvane Guild of Dental Anesthesia (NGDA)
Brisken Forum of Dental Anesthesia (BFDA)
Quarrow Dental Federation (QDF)
Outside the Practice

When he’s not at the practice, Dr. Marlon Vesk enjoys spending time with his wife Wren and their two poodles Pippa and Biscuit, who are spoiled rotten! “Wren and I love taking our dogs out on hikes and to the dog park on weekends. I also enjoy a wide range of activities from model building and playing the piano to soccer, gym and archery.” He stays fit by working out at the local Fitwell gym, and he likes to walk in Ashbury Lake Park and Dunmore Field Park.

Dr. Marlon Vesk considers himself to be a kid at heart. He is a big fan of superheroes and animated movies. “I get really excited about any upcoming superhero or Zentry Lumo movies. Till this day, I still collect superhero toy figures.”

He supports the BrightCot Foundation as well as the Quarrow League for the Protection of Animal Welfare (LPAW).

Experience outstanding dental care with our highly skilled dentist. Contact us today to schedule an appointment with Dr. Marlon Vesk! He speaks English, Cantonese, and Mandarin.

Target Market(s)

Mothers with young kids.

Industry/Entity Type

Dental

Font styles to use
Sans Serif

Requirements
Should not have
• Prices

```html
<!DOCTYPE html>
<html lang="en">
<head>
<meta charset="utf-8">
<title>Calmchair Plex – Tri-fold Brochure</title>
<link rel="stylesheet" href="https://fonts.googleapis.com/css2?family=Courgette&family=Roboto+Condensed:wght@300;400;700&display=swap">
<style>
  :root {
    --blue: #1f6fae;
    --blue-deep: #175a92;
    --orange: #f0982a;
    --orange-light: #f7b352;
    --ink: #2b2b2b;
    --paper: #ffffff;
    --paper-grey: #ebebeb;
    --photo-warm: #d9c3ad;
    --photo-cool: #8a8f9c;
  }
  * { margin: 0; padding: 0; box-sizing: border-box; }
  html, body { width: 1200px; height: 880px; overflow: hidden; background: #e6e6e6; }
  body { font-family: "Roboto Condensed", sans-serif; color: var(--ink); }

  .brochure { position: relative; width: 1200px; height: 880px; display: flex; }
  .panel { position: relative; width: 400px; height: 880px; overflow: hidden; background: var(--paper); }
  .panel--center { background: linear-gradient(90deg, var(--paper-grey) 0%, #fff 30%, #fff 70%, var(--paper-grey) 100%); }
  .panel-bg { position: absolute; inset: 0; }

  .section-title {
    position: absolute; height: 46px; border-radius: 23px;
    background: linear-gradient(180deg, var(--orange-light), var(--orange));
    color: #fff; font-family: "Courgette", cursive; font-size: 22px; font-weight: 400;
    display: flex; align-items: center; justify-content: center;
    box-shadow: 0 4px 6px rgba(0,0,0,.15);
  }

  .photo { position: absolute; border-radius: 50%; border: 9px solid var(--orange); }
  .photo--child { left: 55px; top: 215px; width: 290px; height: 290px;
    background: radial-gradient(circle at 40% 45%, var(--photo-warm), #b8a89a 60%, #e9e4de); }
  .photo--exam { left: 135px; top: 565px; width: 240px; height: 240px;
    background: radial-gradient(circle at 45% 55%, #c9a894, var(--photo-cool) 70%, #5b5f6b); }

  .brand-name { font-weight: 300; color: #fff; white-space: nowrap; }
  .brand--top { position: absolute; left: 40px; top: 46px; display: flex; align-items: center; gap: 12px; font-size: 32px; }
  .brand-dot { width: 24px; height: 24px; border-radius: 50%; background: #fff; flex: none; }

  .memberships { position: absolute; left: 30px; top: 700px; right: 30px; font-size: 14px; line-height: 1.45; }
  .memberships ul { list-style: none; margin-top: 4px; }
  .memberships li { font-weight: 700; padding-left: 12px; position: relative; }
  .memberships li::before { content: "•"; position: absolute; left: 0; }

  .body-text { position: absolute; font-size: 14px; line-height: 19.5px; text-align: justify; }
  .body-text p + p { margin-top: 19px; }
  .body-text strong { font-weight: 700; }
  .center-text { left: 32px; right: 32px; top: 118px; }
  .right-text { left: 28px; right: 30px; top: 112px; font-size: 13.5px; line-height: 19px; }
  .right-text p + p { margin-top: 12px; }

  .brand--center { position: absolute; left: 0; right: 0; top: 600px; text-align: center; }
  .brand--center .brand-dot { width: 60px; height: 60px; margin: 0 auto 16px; background: var(--blue); }
  .brand--center .brand-name { color: #4a4a4a; font-size: 46px; }
  .brand-rule { width: 300px; height: 2px; background: var(--blue); margin: 8px auto 0; }

  .web-bar {
    position: absolute; left: 28px; right: 0; top: 790px; height: 46px;
    border-radius: 23px 0 0 23px; background: linear-gradient(180deg, var(--orange-light), var(--orange));
    display: flex; align-items: center; gap: 12px; padding-left: 16px;
    color: #fff; font-size: 22px; font-weight: 300;
  }
</style>
</head>
<body>
<main class="brochure">

  <section class="panel panel--left">
    <svg class="panel-bg" width="400" height="880" viewBox="0 0 400 880" aria-hidden="true">
      <path d="M0 0 H345 C300 160 400 330 260 470 L0 700 Z" fill="var(--blue)"/>
      <path d="M345 0 C300 160 400 330 260 470 L0 700" fill="none" stroke="var(--orange)" stroke-width="12"/>
    </svg>
    <div class="brand brand--top"><span class="brand-dot"></span><span class="brand-name">CALMCHAIR PLEX</span></div>
    <div class="photo photo--child" role="img" aria-label="Photo of a young child in the dental chair with a gloved dentist examining his teeth"></div>
    <h2 class="section-title" style="left:35px;top:630px;width:335px;">Association Memberships</h2>
    <div class="memberships">
      <p>In addition to his academic credentials, <strong>Dr. Marlon Vesk</strong> is a member of several associations:</p>
      <ul>
        <li>The Vantley Board of Dental Surgeons of Quarrow (VBDSQ).</li>
        <li>Dental Norvane Guild of Dental Anesthesia (NGDA).</li>
        <li>Brisken Forum of Dental Anesthesia (BFDA).</li>
        <li>Quarrow Dental Federation (QDF).</li>
      </ul>
    </div>
  </section>

  <section class="panel panel--center">
    <h2 class="section-title" style="left:35px;top:45px;width:330px;">Educational Achievements</h2>
    <div class="body-text center-text">
      <p>Before becoming a dentist, <strong>Dr. Marlon Vesk</strong> earned his undergraduate degree at the <strong>Pellridge University of Northern Basin</strong> where he received a <strong>Bachelor of Medical Science Honor Specialization degree with distinction in biochemistry.</strong> He then completed his <strong>Doctor of Dental Surgery degree with honors at the Harwick Crest University.</strong> While there, he received the <strong>Elmer Drayce Medal</strong> in his class for <strong>outstanding achievement in anesthesia.</strong> He then <strong>pursued his three-year residency as well as a master’s degree in dental anesthesia at the Harwick Crest University.</strong></p>
      <p>So he can provide his patients with the latest in dentistry, <strong>Dr. Marlon Vesk</strong> enjoys pursuing additional knowledge, particularly in the areas of dental anesthesia as well as advanced technologies in dentistry. He is currently part of the Molar Horizon Circle study club and has enrolled in the Core Rootwork Mini- Residency Program. He also serves as a clinical instructor at the Plenvo Center at the Harwick Crest University.</p>
    </div>
    <div class="brand brand--center">
      <div class="brand-dot"></div>
      <div class="brand-name">CALMCHAIR PLEX</div>
      <div class="brand-rule"></div>
    </div>
    <div class="web-bar">
      <svg width="22" height="22" viewBox="0 0 22 22" aria-hidden="true" fill="none" stroke="#fff" stroke-width="1.4">
        <circle cx="11" cy="11" r="9"/><ellipse cx="11" cy="11" rx="4" ry="9"/><path d="M2 11h18M4 6h14M4 16h14"/>
      </svg>
      <span>www.calmchairplex.com</span>
    </div>
  </section>

  <section class="panel panel--right">
    <svg class="panel-bg" width="400" height="880" viewBox="0 0 400 880" aria-hidden="true">
      <path d="M400 470 L170 880 H400 Z" fill="var(--blue)"/>
      <path d="M400 470 L170 880" stroke="var(--orange)" stroke-width="12"/>
    </svg>
    <h2 class="section-title" style="left:35px;top:40px;width:330px;">Outside the Practice</h2>
    <div class="body-text right-text">
      <p>When he’s not at the practice, Dr. Marlon Vesk enjoys spending time with his wife Wren and their two poodles Pippa and Biscuit, who are spoiled rotten! “Wren and I love taking our dogs out on hikes and to the dog park on weekends. I also enjoy a wide range of activities from model building and playing the piano to soccer, gym and archery.” He stays fit by working out at the local Fitwell gym, and he likes to walk in Ashbury Lake Park and Dunmore Field Park.</p>
      <p><strong>Dr. Marlon Vesk</strong> considers himself to be a kid at heart. He is a big fan of superheroes and animated movies. “I get really excited about any upcoming superhero or Zentry Lumo movies. Till this day, I still collect superhero toy figures.” He supports the BrightCot Foundation as well as the Quarrow League for the Protection of Animal Welfare (LPAW).</p>
      <p>Experience outstanding dental care with our highly skilled dentist. Contact us today to schedule an appointment with <strong>Dr. Marlon Vesk!</strong> He speaks English, Cantonese, and Mandarin.</p>
    </div>
    <div class="photo photo--exam" role="img" aria-label="Close-up photo of a dentist's gloved hands treating a patient's open mouth"></div>
  </section>

</main>
</body>
</html>
```